■依頼の目的/概要
ハルカゼのlumoraで電子書籍出版をします。

■本の内容
40代女性で話すことや伝えること
自分に自信はないけれど

起業したい、
夢や目標を叶えたい、
という方がターゲットです。

声と潜在意識(心)の力を使う「ひだまりトーン」で
人前で自信をもって伝えられるようになったり
やりたいことがどんどん実現できるようになる方法を
書きました。

声や潜在意識を使ったトレーニング、
実例を用いてお伝えしています。

■デザイン要望
40代女性が好むデザインが希望です。
顔写真も入れていただけたらと思います。
その際、手に持っている音符などは載せないようお願いいたします。

お写真と、電子書籍の文章をお送りいたします。

ご応募、心よりお待ちしております!!!

その他何かご不明な点がございましたら、お気軽にご質問下さい。
よろしくお願いいたします。
タイトルは
響きの名手がひもとく
輝く毎日をつくる心の整え方・磨き方
~ひだまりトーンの秘密~

著者は
ひだまりトーンコンサルタント
さとうれな

どうぞよろしくお願いいたします。
LQS表記では、表紙画像のサイズは 50 MB 未満表紙フ
ァイルの理想的な寸法は 2,560 x 1,600 ピクセルとなっています。

文字が見やすいこと。
女性的な優しいイメージと内容が合うもの、
という視点で選ばせていただきました。

素晴らしい作品ばかりで
選ばせていただくのに時間がかかりました。

短期間にも関わらず
素敵な作品を沢山ご応募いただき
どうもありがとうございました!

心より感謝いたします。

機会がございましたら
またどうぞよろしくお願いいたします。

```html
<!DOCTYPE html>
<html lang="ja">
<head>
<meta charset="utf-8">
<title>輝く毎日をつくる心の整え方・磨き方</title>
<link rel="stylesheet" href="https://fonts.googleapis.com/css2?family=M+PLUS+Rounded+1c:wght@500;700;800&display=swap">
<style>
  :root {
    --paper: #ffffff;
    --frame: #d9d9d9;
    --rose: #e6588d;
    --blush: #fbdfe8;
    --ink: #4a3f44;
    --photo-top: #d8c6bd;
    --photo-bottom: #f1e6df;
  }
  html, body {
    margin: 0;
    width: 900px;
    height: 1200px;
    overflow: hidden;
    background: var(--paper);
  }
  .cover {
    position: relative;
    width: 900px;
    height: 1200px;
    box-sizing: border-box;
    border: 3px solid var(--frame);
    background: var(--paper);
    font-family: "M PLUS Rounded 1c", sans-serif;
    color: var(--ink);
  }
  .lead-badge {
    position: absolute;
    left: 315px;
    top: 22px;
    width: 270px;
    height: 215px;
    border-radius: 50%;
    background: var(--blush);
    display: flex;
    flex-direction: column;
    align-items: center;
    justify-content: center;
    font-weight: 700;
    font-size: 27px;
    line-height: 1.35;
    text-align: center;
    white-space: nowrap;
  }
  .title-column {
    position: absolute;
    margin: 0;
    display: flex;
    flex-direction: column;
    align-items: center;
    width: 180px;
    color: var(--rose);
    font-weight: 800;
    font-size: 160px;
    line-height: 180px;
  }
  .title-column.left { left: 75px; top: 280px; }
  .title-column.right { left: 645px; top: 215px; }
  .title-core {
    position: absolute;
    left: 350px;
    top: 420px;
    width: 230px;
    height: 145px;
    box-sizing: border-box;
    border: 5px solid var(--rose);
    border-radius: 18px;
    display: flex;
    align-items: center;
    justify-content: center;
    font-weight: 800;
    font-size: 74px;
    white-space: nowrap;
  }
  .author {
    position: absolute;
    left: 470px;
    top: 605px;
    width: 180px;
    text-align: center;
    white-space: nowrap;
  }
  .author-role {
    font-weight: 700;
    font-size: 16px;
    line-height: 1.35;
  }
  .author-name {
    margin-top: 4px;
    color: var(--rose);
    font-weight: 800;
    font-size: 28px;
    letter-spacing: 1px;
  }
  .portrait {
    position: absolute;
    left: 345px;
    top: 740px;
    width: 210px;
    height: 210px;
    border-radius: 50%;
    background: linear-gradient(180deg, var(--photo-top), var(--photo-bottom));
  }
  .series-band {
    position: absolute;
    left: 100px;
    top: 1080px;
    width: 700px;
    height: 62px;
    background: var(--blush);
    display: flex;
    align-items: center;
    justify-content: center;
    font-weight: 800;
    font-size: 40px;
    letter-spacing: 2px;
    white-space: nowrap;
  }
</style>
</head>
<body>
  <main class="cover">
    <div class="lead-badge">
      <span>響きの名手が</span>
      <span>ひもとく</span>
      <span>輝く毎日をつくる</span>
    </div>

    <h1 class="title-column left" aria-label="磨き方">
      <span>磨</span><span>き</span><span>方</span>
    </h1>
    <div class="title-core">心の</div>
    <h1 class="title-column right" aria-label="整え方">
      <span>整</span><span>え</span><span>方</span>
    </h1>

    <div class="author">
      <div class="author-role">ひだまりトーン<br>コンサルタント</div>
      <div class="author-name">さとうれな</div>
    </div>

    <div class="portrait" role="img" aria-label="著者さとうれなの顔写真"></div>

    <div class="series-band">ひだまりトーンの秘密</div>
  </main>
</body>
</html>
```